Harbor of Embers How a Quiet Mill Town Found Its Second Song.

This compelling story deserves a great cover which conveys transformation. As a pastor, I started a church in the financial district of Atlanta. What began as a typical "church plant" became an adventure in risk, creativity, and the building was a beautiful metaphor of transformation as we took a closed down strip club and turned it into a church venue. Our group learned many lessons about accepting people from all sorts of backgrounds, and about seeing God's power at work. I envision a cover which communicates transformation, perhaps using darkness and light, or maybe using the Rivet Lounge building being painted. It was a solid black building (with gold trim) and we painted it white, with a blue logo of the church name. I need book cover, spine, and back, along with whatever is needed for Brindlemart to accept it for their site.

```html
<!DOCTYPE html>
<html lang="en">
<head>
<meta charset="utf-8">
<title>Harbor of Embers – Cover Spread</title>
<link href="https://fonts.googleapis.com/css2?family=Montserrat:wght@400;500;600;700;800&family=Allura&display=swap" rel="stylesheet">
<style>
  :root{
    --page:#ffffff;
    --cover-top:#2b2b2e;
    --cover-bottom:#121318;
    --gold-light:#fbefb0;
    --gold-mid:#e0b73c;
    --gold-deep:#a9872f;
    --ember:#e84a2a;
    --ink:#ffffff;
    --box:#ffffff;
    --box-ink:#333333;
  }
  *{box-sizing:border-box;margin:0;padding:0}
  html,body{width:1200px;height:2266px;overflow:hidden;background:var(--page)}
  body{position:relative;font-family:"Montserrat",sans-serif;color:var(--ink)}

  .spread{
    position:absolute;left:94px;top:123px;width:1007px;height:697px;
    background:linear-gradient(180deg,var(--cover-top) 0%,#1d1e22 55%,var(--cover-bottom) 100%);
    overflow:hidden;
  }
  .abs{position:absolute}

  .gold{
    background:linear-gradient(180deg,var(--gold-light) 0%,var(--gold-mid) 45%,var(--gold-deep) 100%);
    -webkit-background-clip:text;background-clip:text;color:transparent;
  }
  .title-word{font-weight:800;letter-spacing:-2px;line-height:1;white-space:nowrap;text-align:center}
  .title-script{font-family:"Allura",cursive;color:var(--gold-mid);line-height:1;white-space:nowrap;text-align:center}

  /* front cover */
  .front-title-top{left:586px;width:380px;top:130px;font-size:74px}
  .front-script{left:586px;width:380px;top:180px;font-size:46px}
  .front-title-bottom{left:586px;width:380px;top:214px;font-size:74px}
  .front-subtitle{left:586px;width:380px;top:290px;font-size:17px;font-weight:600;text-align:center}
  .front-band{left:651px;top:316px;width:250px;height:20px;background:var(--ember);
    font-size:16px;font-weight:600;text-align:center;line-height:20px;white-space:nowrap}
  .front-illustration{left:590px;top:362px;width:346px;height:223px;
    background:radial-gradient(ellipse at 50% 60%,rgba(170,140,70,.35) 0%,rgba(120,100,55,.15) 50%,rgba(0,0,0,0) 75%)}
  .front-rule{left:736px;top:607px;width:71px;height:3px;background:var(--ember)}
  .front-author{left:586px;width:380px;top:628px;font-size:23px;font-weight:700;text-align:center;letter-spacing:.5px}

  /* spine */
  .spine-line{writing-mode:vertical-rl;white-space:nowrap;font-size:11.5px;font-weight:500}
  .spine-sub-1{left:505px;top:123px}
  .spine-sub-2{left:485px;top:123px;background:var(--ember);padding:2px 1px}
  .spine-title{left:484px;top:322px;writing-mode:vertical-rl;font-weight:800;font-size:18px;line-height:.95;letter-spacing:-.5px;white-space:nowrap}
  .spine-rule{left:502px;top:415px;width:2px;height:12px;background:var(--ember)}
  .spine-author{left:490px;top:440px;writing-mode:vertical-rl;font-size:15px;font-weight:700;letter-spacing:.5px;white-space:nowrap}

  /* back cover */
  .back-title-top{left:130px;width:210px;top:133px;font-size:44px}
  .back-script{left:130px;width:210px;top:158px;font-size:28px}
  .back-title-bottom{left:130px;width:210px;top:180px;font-size:44px}
  .back-copy{left:41px;width:405px;font-size:11.3px;line-height:16px;font-weight:400}
  .back-copy-1{top:262px}
  .back-copy-2{top:350px}
  .back-bio{left:129px;top:464px;width:300px;font-size:11.3px;line-height:16px}
  .author-photo{left:39px;top:467px;width:82px;height:86px;background:var(--box);color:var(--box-ink);
    font-size:10px;line-height:12px;display:flex;align-items:center;justify-content:center;text-align:center}
  .isbn-box{left:283px;top:580px;width:145px;height:73px;background:var(--box);color:var(--box-ink);
    font-size:12px;display:flex;align-items:center;justify-content:center}
</style>
</head>
<body>
  <main class="spread">
    <section class="back-cover">
      <div class="abs title-word gold back-title-top">HARBOR</div>
      <div class="abs title-script back-script">of</div>
      <div class="abs title-word gold back-title-bottom">EMBERS</div>
      <p class="abs back-copy back-copy-1">Lorem Ipsum is simply dummy text of the printing and typesetting industry. Lorem Ipsum has been the industry's standard dummy text ever since the 1500s, when an Lorem Ipsum passags, and more recently with desktop pubng software like Quillset Layout includi versions of Lorem Ipsum.</p>
      <p class="abs back-copy back-copy-2">Lorem Ipsum is simply dummy text of the printing and typesetting industry. Lorem Ipsum has been the industry's standard dummy text ever since the 1500s, when an Lorem Ipsum passags, and more recently with desktop pubng software like Quillset Layout includi versions of Lorem Ipsum. Lorem Ipsum is simply dummy text of the printing and typesetting industry.</p>
      <div class="abs author-photo">author<br>image</div>
      <p class="abs back-bio">Lorem Ipsum is simply dummy text of the printing and typesetting industry. Lorem Ipsum has been the industry's standard dummy text ever since the 1500s, when an Lorem Ipsum passags, and more recently with desktop pubng software like Quillset Layout includi versions of Lorem Ipsum.</p>
      <div class="abs isbn-box">ISBN</div>
    </section>

    <section class="spine">
      <div class="abs spine-line spine-sub-1">How a Quiet Mill Town</div>
      <div class="abs spine-line spine-sub-2">Found Its Second Song.</div>
      <div class="abs spine-title gold">HARBOR<br>EMBERS</div>
      <div class="abs spine-rule"></div>
      <div class="abs spine-author">AUTHOR NAME</div>
    </section>

    <section class="front-cover">
      <div class="abs title-word gold front-title-top">HARBOR</div>
      <div class="abs title-script front-script">of</div>
      <div class="abs title-word gold front-title-bottom">EMBERS</div>
      <div class="abs front-subtitle">How a Quiet Mill Town</div>
      <div class="abs front-band">Found Its Second Song.</div>
      <div class="abs front-illustration" role="img" aria-label="Gold line drawing of the converted lounge building, now a church"></div>
      <div class="abs front-rule"></div>
      <div class="abs front-author">AUTHOR NAME</div>
    </section>
  </main>
</body>
</html>
```